New Web Design Project

Require a website for The Marrow Orchard. All relevant information is in the uploaded files.

website to be responsive to work on mobile.

Required in html5, css

Coding

Coded - Design and coding required

Number of Pages Required

3 page

```html
<!DOCTYPE html>
<html lang="en">
<head>
<meta charset="utf-8">
<title>The Marrow Orchard</title>
<link href="https://fonts.googleapis.com/css2?family=Poppins:ital,wght@0,300;0,400;0,500;0,600;1,400&family=Ubuntu:wght@700&display=swap" rel="stylesheet">
<style>
:root{
  --green:#8cc63f;
  --orange:#f7941d;
  --ink:#1d2a2e;
  --header:#1c2529;
  --text:#555d61;
  --muted:#9aa0a3;
  --panel:#f6f6f6;
  --line:#e3e3e3;
  --footer:#1a2127;
  --white:#ffffff;
}
*{box-sizing:border-box;margin:0;padding:0}
html,body{width:1200px;height:2715px;overflow:hidden}
body{position:relative;font-family:'Poppins',sans-serif;color:var(--text);background:var(--white)}
.abs{position:absolute}

/* header */
.topline{left:0;top:0;width:1200px;height:8px;background:var(--green)}
.header{left:0;top:8px;width:1200px;height:67px;background:var(--header)}
.brand{left:0;top:0;width:290px;height:82px;background:var(--white);border-radius:0 0 42px 0;display:flex;align-items:center;justify-content:center;gap:8px;z-index:3}
.brand-dot{width:22px;height:22px;border-radius:50%;background:var(--orange)}
.brand-name{font-weight:600;font-size:16px;color:var(--ink)}
.nav{left:428px;top:35px;display:flex;gap:21px;font-size:11.5px;color:#e8ecee;z-index:3}
.nav .active{color:var(--green)}
.call{left:848px;top:25px;display:flex;align-items:center;gap:9px;z-index:3}
.call-icon{width:32px;height:32px;border-radius:50%;background:var(--orange)}
.call small{display:block;font-size:10px;color:var(--green)}
.call strong{display:block;font-size:15px;font-weight:400;color:var(--white)}
.header-social{left:1007px;top:28px;display:flex;gap:6px;z-index:3}
.header-social span{width:29px;height:29px;border-radius:50%;border:1px solid #6c7478}
.header-social span:first-child{border-color:var(--green)}
.divider{left:993px;top:28px;width:1px;height:30px;background:#4b5458;z-index:3}

/* hero */
.hero-photo{left:0;top:75px;width:1200px;height:715px;background:linear-gradient(100deg,#8a8f86 0%,#a9a99e 30%,#c9d3d8 55%,#7fa7c6 75%,#2c3035 100%)}
.hero-wave{left:0;top:0;width:1200px;height:800px}
.hero-title{left:158px;top:240px;font-family:'Ubuntu',sans-serif;font-weight:700;font-size:58px;line-height:56px;color:var(--ink);letter-spacing:1px}
.hero-title em{font-style:normal;color:var(--green)}
.hero-text{left:159px;top:364px;width:430px;font-size:13.5px;line-height:21px;color:var(--white)}
.btn{display:inline-flex;align-items:center;justify-content:center;background:var(--orange);color:var(--white);font-weight:500;font-size:15px;letter-spacing:.5px;border-radius:20px}
.hero-btn{left:161px;top:419px;width:143px;height:37px}
.hero-arrow{left:54px;top:333px;width:12px;height:18px}

/* about */
.about-icon{left:585px;top:758px;width:30px;height:30px;border-radius:50%;background:var(--orange)}
.section-title{font-weight:600;color:var(--ink);font-size:34px;text-align:center}
.about-title{left:0;top:808px;width:1200px}
.about-copy{left:325px;top:873px;width:550px;text-align:center;font-size:11.5px;line-height:19.5px;color:var(--text)}
.about-copy p{margin-bottom:12px}
.about-cta{left:400px;top:1071px;width:400px;text-align:center;font-style:italic;font-size:15px;line-height:24px;color:var(--orange)}

/* people */
.people-band{left:0;top:1212px;width:1200px;height:460px;background:var(--panel)}
.skyline{left:0;top:1165px;width:1200px;height:90px;background:linear-gradient(180deg,rgba(230,230,230,0) 0%,#e9e9e9 40%,#eeeeee 100%)}
.people-title{left:0;top:1300px;width:1200px}
.card{top:1393px;height:198px;background:var(--white)}
.card-left{left:163px;width:413px}
.card-right{left:727px;width:413px}
.portrait{width:212px;height:212px}
.name{font-weight:500;font-size:19px;color:var(--ink)}
.role{font-size:12.5px;color:var(--orange)}
.link{font-size:14px;line-height:23px;color:#2a7fd6;text-decoration:underline;width:240px;word-break:break-all}

/* social */
.social-title{left:0;top:1743px;width:1200px}
.follow{left:0;top:1794px;width:1200px;text-align:center;font-size:13px;color:var(--text)}
.social-btn{top:1842px;width:135px;height:40px;border-radius:20px;display:flex;align-items:center;gap:10px;padding-left:18px;color:var(--white);font-size:11.5px;font-weight:600;letter-spacing:.4px}
.social-btn i{width:12px;height:12px;border-radius:50%;background:rgba(255,255,255,.85)}
.fb{left:302px;background:#3b5998}
.tw{left:455px;background:#1da1f2}
.li{left:609px;background:#1b74b8}
.ig{left:763px;background:linear-gradient(90deg,#f5b333,#e1306c 60%,#b12aa6)}

/* contact */
.footer-shape{left:0;top:2180px;width:1200px;height:500px}
.contact-card{left:284px;top:1941px;width:631px;height:477px;background:var(--white);box-shadow:0 0 14px rgba(0,0,0,.08)}
.contact-title{left:337px;top:1991px;font-weight:600;font-size:34px;color:var(--ink)}
.contact-sub{left:338px;top:2037px;font-size:12.5px;color:var(--text)}
.field{height:37px;border:1px solid var(--line);border-radius:19px;background:linear-gradient(180deg,#f3f3f3,#ffffff);font-size:11.5px;color:var(--muted);padding:10px 16px}
.field.focus{border-color:var(--green);color:var(--green);background:var(--white)}
.f1{left:337px;top:2081px;width:255px}
.f2{left:608px;top:2081px;width:254px}
.f3{left:337px;top:2130px;width:255px}
.f4{left:608px;top:2130px;width:254px}
.f5{left:337px;top:2178px;width:525px;height:75px;border-radius:20px}
.caret{left:842px;top:2148px;width:0;height:0;border-left:4px solid transparent;border-right:4px solid transparent;border-top:5px solid var(--orange)}
.captcha{left:339px;top:2263px;width:226px;height:58px;border:1px solid #d3d3d3;border-radius:3px;background:#f9f9f9;display:flex;align-items:center;gap:12px;padding-left:12px;font-size:12px;color:#222}
.captcha i{width:20px;height:20px;border:2px solid #c1c1c1;border-radius:2px;background:var(--white)}
.contact-btn{left:333px;top:2333px;width:142px;height:36px}

/* footer */
.footer-photo{left:0;top:2418px;width:1200px;height:251px;background:linear-gradient(180deg,#1d252b,#172026 60%,#1e2630)}
.foot-brand{left:61px;top:2463px;display:flex;align-items:center;gap:8px}
.foot-brand i{width:30px;height:30px;border-radius:50%;background:var(--orange)}
.foot-brand span{font-weight:600;font-size:18px;color:var(--white)}
.foot-about{left:61px;top:2527px;width:250px;font-size:11.5px;line-height:20px;color:#b7bcbf}
.foot-head{top:2470px;font-weight:600;font-size:13px;color:var(--white);letter-spacing:.3px}
.foot-links{left:337px;top:2500px;list-style:none;font-size:11px;line-height:24px;color:#b7bcbf}
.foot-links li::before{content:"";display:inline-block;width:4px;height:4px;border-radius:50%;background:var(--orange);margin:0 12px 2px 1px;vertical-align:middle}
.foot-contact{left:612px;top:2500px;font-size:11px;color:#b7bcbf}
.foot-contact .row{display:flex;gap:14px;margin-bottom:12px}
.foot-contact svg{width:15px;height:15px;margin-top:4px;flex:none}
.foot-contact b{display:block;font-weight:400;font-size:12.5px;color:var(--white)}
.foot-social{left:887px;top:2506px;display:flex;gap:5px}
.foot-social span{width:37px;height:37px;border-radius:50%}
.copyright{left:0;top:2669px;width:1200px;height:46px;background:var(--green);color:var(--white);font-size:11.5px;display:flex;align-items:center;justify-content:center}
</style>
</head>
<body>

<div class="abs hero-photo" role="img" aria-label="Smiling businessman in glasses sitting outdoors holding a tablet"></div>
<svg class="abs hero-wave" viewBox="0 0 1200 800" aria-hidden="true">
  <path d="M0,560 C80,610 160,635 230,612 C300,585 360,560 410,590 C455,618 460,692 520,695 C575,698 585,650 640,660 C720,672 780,765 880,780 C980,792 1070,725 1200,770 L1200,800 L0,800 Z" fill="#ffffff"/>
  <path d="M0,532 C70,590 150,635 235,612" fill="none" stroke="#f7941d" stroke-width="9"/>
  <path d="M460,690 C480,665 540,645 590,655" fill="none" stroke="#8cc63f" stroke-width="8"/>
  <path d="M840,778 C960,790 1060,712 1200,765" fill="none" stroke="#f7941d" stroke-width="9"/>
</svg>

<div class="abs topline"></div>
<div class="abs header"></div>
<div class="abs brand"><span class="brand-dot"></span><span class="brand-name">The Marrow Orchard</span></div>
<nav class="abs nav"><span class="active">HOME</span><span>ABOUT US</span><span>PEOPLE</span><span>SOCIAL MEDIA</span><span>CONTACT</span></nav>
<div class="abs call"><span class="call-icon"></span><div><small>Call Us On :</small><strong>555 014 2270</strong></div></div>
<div class="abs divider"></div>
<div class="abs header-social"><span></span><span></span><span></span><span></span></div>

<h1 class="abs hero-title">LET CONSULT<br>WITH<em>EXPERTS</em></h1>
<p class="abs hero-text">The Marrow Orchard was incorporated with Canadian market through a trusted and mutual business relation</p>
<a class="abs btn hero-btn">CONTACT US</a>
<svg class="abs hero-arrow" viewBox="0 0 12 18" aria-hidden="true"><path d="M10,1 L2,9 L10,17" fill="none" stroke="#ffffff" stroke-width="1.5"/></svg>

<section>
  <div class="abs about-icon"></div>
  <h2 class="abs section-title about-title">About Us</h2>
  <div class="abs about-copy">
    <p>The Marrow Orchard was incorporated with the objective of introducing new vendors to the Canadian market through a trusted and mutual business relation</p>
    <p>It was set up by Dario Venn and Milo Kastra who have a combined experience of over 45 years in the fresh produce business. With Dario's expertise in global sourcing and Milo's vast connection and know how of the Canadian market, we have helped our existing partners grow and expand their reach in the Canadian fresh produce market.</p>
    <p>Our expertise andsupply chain knowledge allow us to develop programs and introduce new products to the Canadian consumer, via retail and wholesale channels across Canada</p>
  </div>
  <p class="abs about-cta">Get in touch to discuss how we can add value to<br>your business</p>
</section>

<section>
  <div class="abs people-band"></div>
  <div class="abs skyline" role="img" aria-label="Faint grey city skyline silhouette"></div>
  <h2 class="abs section-title people-title">People</h2>

  <div class="abs card card-left"></div>
  <svg class="abs portrait" style="left:60px;top:1386px" viewBox="0 0 212 212">
    <circle cx="106" cy="106" r="101" fill="none" stroke="#2b3134" stroke-width="6"/>
    <path d="M140,11 A101,101 0 1,1 40,182" fill="none" stroke="#8cc63f" stroke-width="6"/>
    <circle cx="106" cy="106" r="90" fill="#b9b6b2" role="img" aria-label="Portrait of Dario Venn in a dark suit"/>
  </svg>
  <div class="abs name" style="left:297px;top:1430px">Dario Venn</div>
  <div class="abs role" style="left:298px;top:1457px">Founder &amp; President</div>
  <div class="abs link" style="left:299px;top:1494px">https://www.example.com/in/dario-venn-41</div>

  <div class="abs card card-right"></div>
  <svg class="abs portrait" style="left:624px;top:1386px" viewBox="0 0 212 212">
    <circle cx="106" cy="106" r="101" fill="none" stroke="#2b3134" stroke-width="6"/>
    <path d="M140,11 A101,101 0 1,1 40,182" fill="none" stroke="#8cc63f" stroke-width="6"/>
    <circle cx="106" cy="106" r="90" fill="#8f8a86" role="img" aria-label="Portrait of Milo Kastra in a dark jacket"/>
  </svg>
  <div class="abs name" style="left:861px;top:1430px">Milo Kastra</div>
  <div class="abs role" style="left:862px;top:1457px">Founder</div>
  <div class="abs link" style="left:863px;top:1494px">https://www.example.com/in/milo-kastra-72/</div>
</section>

<section>
  <h2 class="abs section-title social-title">Social Media</h2>
  <p class="abs follow">Follow Us On</p>
  <a class="abs social-btn fb"><i></i>FEEDSPOT</a>
  <a class="abs social-btn tw"><i></i>CHIRPLY</a>
  <a class="abs social-btn li"><i></i>WORKLINE</a>
  <a class="abs social-btn ig"><i></i>PHOTOLANE</a>
</section>

<svg class="abs footer-shape" viewBox="0 0 1200 500" aria-hidden="true">
  <path d="M0,115 C90,65 190,35 284,20 L284,238 L915,238 L915,108 L1200,288 L1200,500 L0,500 Z" fill="#1a2127"/>
</svg>
<div class="abs footer-photo" role="img" aria-label="Dark aerial view of a city at dusk"></div>

<section>
  <div class="abs contact-card"></div>
  <h2 class="abs contact-title">Contact Us</h2>
  <p class="abs contact-sub">Have an any question for contact us Today !</p>
  <div class="abs field focus f1">Name *</div>
  <div class="abs field f2">Email *</div>
  <div class="abs field f3">Email*</div>
  <div class="abs field f4">Consult With *</div>
  <div class="abs caret"></div>
  <div class="abs field f5">Message *</div>
  <div class="abs captcha"><i></i>I'm not a robot</div>
  <a class="abs btn contact-btn">CONTACT US</a>
</section>

<footer>
  <div class="abs foot-brand"><i></i><span>The Marrow Orchard</span></div>
  <p class="abs foot-about">The Marrow Orchard was incorpora - ted with the objective of introducing new vendors to the Canadian...</p>

  <div class="abs foot-head" style="left:337px">SITEMAP</div>
  <ul class="abs foot-links"><li>Home</li><li>About Us</li><li>People</li><li>Social Media</li><li>Contact Us</li></ul>

  <div class="abs foot-head" style="left:612px">CONTACT US</div>
  <div class="abs foot-contact">
    <div class="row"><svg viewBox="0 0 16 16"><path d="M3,1 L6,1 L7,5 L5,6.5 C6,9 7.5,10.5 10,11.5 L11.5,9.5 L15,10.5 L15,13.5 C15,14.5 14,15 13,15 C6,14 2,10 1,3 C1,2 2,1 3,1 Z" fill="#f7941d"/></svg><div>Dario Venn<b>+1 555 014 2270</b></div></div>
    <div class="row"><svg viewBox="0 0 16 16"><path d="M3,1 L6,1 L7,5 L5,6.5 C6,9 7.5,10.5 10,11.5 L11.5,9.5 L15,10.5 L15,13.5 C15,14.5 14,15 13,15 C6,14 2,10 1,3 C1,2 2,1 3,1 Z" fill="#f7941d"/></svg><div>Milo Kastra<b>+1 555 014 2270</b></div></div>
    <div class="row"><svg viewBox="0 0 16 16"><rect x="1" y="3" width="14" height="10" rx="1" fill="#f7941d"/><path d="M1,4 L8,9 L15,4" fill="none" stroke="#1a2127" stroke-width="1.3"/></svg><div><b style="margin-top:2px">hello@marroworchard.com</b></div></div>
  </div>

  <div class="abs foot-head" style="left:887px">FOLLOW US</div>
  <div class="abs foot-social">
    <span style="background:#3b5998"></span><span style="background:#1da1f2"></span><span style="background:#1b74b8"></span><span style="background:linear-gradient(135deg,#f5b333,#e1306c,#b12aa6)"></span>
  </div>

  <div class="abs copyright">©The Marrow Orchard -2020 All rights reserved. Privacy policy &nbsp;|&nbsp; Tearms &amp; Conditions</div>
</footer>

</body>
</html>
```